Photography Business Card Design

I want a simple,classy design using a logo and simple font such as minion pro or similar. I have attached a logo that I quite like or am open to something similar. On the back of the card I would like the attached photo possibly with my website address on it some where. I want a matt black with silver or grey print. Possibly have the logo off to one side with the words Daniel Festerby Photography stacked on top of each other
Updates
I am very sorry that some how I forgot to put my facebook address on the details section, www.socialpage.example/DanielFesterbyPhotography
If this could be include on the card as well.
Industry/Entity Type
Business
Contact Information for Business Card
Daniel Festerby Photography
www.danielfesterbyphotography.example.au
Email: danielfesterby@wirenest.example
Phone: +61 (0)427 318 502
Logo Text
Logo styles of interest
Abstract Logo
Look and feel

```html
<!DOCTYPE html>
<html lang="en">
<head>
<meta charset="utf-8">
<title>Daniel Festerby Photography – Business Card</title>
<link href="https://fonts.googleapis.com/css2?family=Crimson+Pro:ital,wght@0,400;0,600;0,700;1,400&display=swap" rel="stylesheet">
<style>
  :root {
    --card-black: #000000;
    --silver-light: #d2d2d2;
    --silver-mid: #9a9a9a;
    --grey-name: #7b7b7b;
    --grey-detail: #8a8a8a;
    --white: #ffffff;
    --photo-light: #a8a8a8;
    --photo-mid: #4a4a4a;
    --photo-dark: #0c0c0c;
  }
  html, body {
    margin: 0;
    padding: 0;
    width: 1200px;
    height: 693px;
    overflow: hidden;
    background: var(--card-black);
  }
  .card {
    position: relative;
    width: 1200px;
    height: 693px;
    background: var(--card-black);
    font-family: "Crimson Pro", "Times New Roman", serif;
    overflow: hidden;
  }
  .card-photo {
    position: absolute;
    left: 0;
    top: 0;
    width: 565px;
    height: 693px;
    background: linear-gradient(155deg, var(--photo-light) 0%, var(--photo-mid) 40%, var(--photo-dark) 85%);
  }
  .brand-mark {
    position: absolute;
    left: 822px;
    top: 96px;
    width: 112px;
    height: 112px;
    background: var(--grey-name);
  }
  .business-name {
    position: absolute;
    left: 660px;
    top: 222px;
    margin: 0;
    color: var(--grey-name);
    font-size: 56px;
    font-weight: 700;
    line-height: 1;
    letter-spacing: 0.5px;
  }
  .business-tagline {
    position: absolute;
    left: 664px;
    top: 286px;
    margin: 0;
    color: var(--grey-name);
    font-size: 32px;
    font-style: italic;
    font-weight: 400;
    letter-spacing: 22px;
    line-height: 1;
  }
  .web-links {
    position: absolute;
    left: 656px;
    top: 402px;
    line-height: 1;
  }
  .web-links .website {
    display: block;
    color: var(--silver-light);
    font-size: 25px;
  }
  .web-links .social {
    display: block;
    margin-top: 8px;
    color: var(--silver-mid);
    font-size: 22.5px;
  }
  .contact-details {
    position: absolute;
    left: 656px;
    top: 538px;
    line-height: 1;
  }
  .contact-details .email {
    display: block;
    color: var(--grey-detail);
    font-size: 27px;
  }
  .contact-details .phone {
    display: block;
    margin-top: 8px;
    color: var(--grey-detail);
    font-size: 31px;
  }
  .contact-details .phone-number {
    color: var(--white);
  }
</style>
</head>
<body>
  <main class="card">
    <div class="card-photo" role="img" aria-label="Black and white landscape photograph of tall pine trees on a hillside under a cloudy sky"></div>

    <div class="brand-mark" aria-hidden="true"></div>

    <h1 class="business-name">Daniel Festerby</h1>
    <p class="business-tagline">Photography</p>

    <div class="web-links">
      <span class="website">www.danielfesterbyphotography.example.au</span>
      <span class="social">www.socialpage.example/DanielFesterbyPhotography</span>
    </div>

    <div class="contact-details">
      <span class="email">Email: danielfesterby@wirenest.example</span>
      <span class="phone">Phone: <span class="phone-number">+61 (0)427 318 502</span></span>
    </div>
  </main>
</body>
</html>
```